Broschüre für Konzepte rund um Immobilien
Zielgruppe
Wir sind ein junges, dynamisches Team und unterstützen Kunden mit individuellen, abgestimmten Konzepten rund um Ihre Immobilie - daher suchen wir ein hochwertiges Design, unsere Zielgruppe liegt Wert auf was neues, nicht das was jeder hat.
Aufgabenstellung
Die Farben und das Layout sollen von der Homepage übernommen werden www.k7-zelt.de..
Den Text entnehmen Sie der angehängten Datei. Bilder, Anordnungen und sonstiges überlasse ich Ihren kreativen Geist! DIN A5 Querformat - Bilder und Texte müssen in einer sehr hohen Auflösung umsetzbar sein!

```html
<!DOCTYPE html>
<html lang="de">
<head>
<meta charset="utf-8">
<title>K7ZELT – Broschüre</title>
<link href="https://fonts.googleapis.com/css2?family=Archivo+Narrow:wght@600;700&family=Work+Sans:wght@400;500&display=swap" rel="stylesheet">
<style>
  :root {
    --backdrop: #434343;
    --paper: #ffffff;
    --ink: #1e1f2c;
    --muted: #8a8a8e;
    --room-light: #f2f2f2;
    --room-mid: #c9c9c9;
    --room-wood: rgba(150, 112, 74, 0.75);
    --room-rug: rgba(52, 52, 54, 0.8);
    --room-sofa: rgba(235, 235, 235, 0.9);
    --concrete-a: #6a6a6a;
    --concrete-b: #505050;
    --concrete-c: #242424;
  }
  * { margin: 0; padding: 0; box-sizing: border-box; }
  html, body { width: 1200px; height: 845px; overflow: hidden; background: var(--backdrop); }
  body { position: relative; font-family: "Work Sans", sans-serif; color: var(--ink); }

  .page { position: absolute; background: var(--paper); }
  .spread-text { left: 7px; top: 3px; width: 458px; height: 416px; }
  .back-cover { left: 302px; top: 428px; width: 459px; height: 417px; }

  .photo { position: absolute; }
  .photo-living-room {
    left: 465px; top: 3px; width: 724px; height: 416px;
    background:
      radial-gradient(ellipse 45% 40% at 50% 72%, var(--room-sofa) 0%, rgba(235,235,235,0) 100%),
      radial-gradient(ellipse 40% 45% at 78% 88%, var(--room-rug) 0%, rgba(52,52,54,0) 100%),
      radial-gradient(ellipse 30% 45% at 10% 78%, var(--room-wood) 0%, rgba(150,112,74,0) 100%),
      radial-gradient(ellipse 28% 35% at 92% 60%, var(--room-wood) 0%, rgba(150,112,74,0) 100%),
      radial-gradient(ellipse 45% 40% at 58% 22%, #ffffff 0%, rgba(255,255,255,0) 100%),
      linear-gradient(180deg, var(--room-light) 0%, #e2e2e2 45%, var(--room-mid) 100%);
  }
  .photo-concrete {
    left: 761px; top: 428px; width: 132px; height: 417px;
    background:
      radial-gradient(ellipse 35% 30% at 90% 18%, rgba(170,170,170,0.7) 0%, rgba(170,170,170,0) 100%),
      linear-gradient(180deg, var(--concrete-a) 0%, var(--concrete-b) 55%, var(--concrete-c) 100%);
  }

  .step-title {
    position: absolute; font-family: "Archivo Narrow", sans-serif; font-weight: 700;
    font-size: 9.2px; line-height: 11px; text-align: right; white-space: nowrap;
  }
  .step-label {
    position: absolute; font-family: "Archivo Narrow", sans-serif; font-weight: 600;
    font-size: 6.5px; line-height: 8px; color: var(--muted); text-align: right; white-space: nowrap;
  }
  .step-text {
    position: absolute; font-size: 7.3px; line-height: 10.95px; font-weight: 500;
    white-space: nowrap; letter-spacing: -0.05px;
  }
  .brand-mention { color: var(--muted); }

  .step-4 .step-title { right: 222px; top: 89px; }
  .step-4 .step-label { right: 223px; top: 102px; }
  .step-4 .step-text { left: 247px; top: 111px; }

  .step-5 .step-title { right: 318px; top: 231px; }
  .step-5 .step-label { right: 318px; top: 244px; }
  .step-5 .step-text { left: 152px; top: 254px; }

  .brand-mark { position: absolute; left: 164px; top: 236px; width: 34px; text-align: center; }
  .brand-mark .dot { display: block; width: 14px; height: 14px; margin: 0 auto 3px; border-radius: 50%; background: var(--muted); }
  .brand-mark .name { font-size: 6px; font-weight: 500; color: var(--muted); letter-spacing: 0.2px; }

  .contact { position: absolute; left: 219px; top: 250px; font-style: normal; }
  .contact .company { font-family: "Archivo Narrow", sans-serif; font-weight: 700; font-size: 8px; line-height: 10px; margin-bottom: 13px; }
  .contact .line { font-size: 6.2px; line-height: 10.95px; color: var(--muted); font-weight: 500; }
</style>
</head>
<body>
  <section class="page spread-text">
    <article class="step step-4">
      <h2 class="step-title">Ihre Planung ist fertig</h2>
      <p class="step-label">Schritt 4</p>
      <p class="step-text">Sie treffen sich nach circa vier Wochen<br>wieder. Gemeinsam mit unserem<br>Berater gehen Sie nun zu unseren<br>Partnerfirmen um das gesamte<br>Gestaltungskonzept durchzugehen und<br>Details nochmals abzustimmen.<br>Inhaltliche und organisatorische Fragen<br>für die Umsetzung werden geklärt.</p>
    </article>
    <article class="step step-5">
      <h2 class="step-title">In Verbindung bleiben</h2>
      <p class="step-label">Schritt 5</p>
      <p class="step-text">Nun haben Sie alle Möglichkeiten, Ihre<br>individuelle Raumgestaltung umzuset-<br>zen. <span class="brand-mention">K7ZELT</span> unterstützt Sie weiterhin<br>gerne im Bereich Möbel- und Küchen-<br>konzepte. Wann und wie Sie Empfeh-<br>lungen oder das gesamte Konzept<br>verwirklichen, entscheiden Sie selbst…</p>
    </article>
  </section>
  <div class="photo photo-living-room" role="img" aria-label="Helles Wohnzimmer in Schwarz-Weiß mit Ecksofa, gemusterten Kissen, Kaktus, Stehlampe, Holzboden, dunklem Teppich und großem Fenster"></div>

  <section class="page back-cover">
    <div class="brand-mark">
      <span class="dot"></span>
      <span class="name">K7ZELT</span>
    </div>
    <address class="contact">
      <p class="company">K7ZELT</p>
      <p class="line">Lindenhofer Gasse 14</p>
      <p class="line">56410 Montabaur</p>
      <p class="line">02602-4718305</p>
      <p class="line">info@k7-zelt.de</p>
      <p class="line">www.k7-zelt.de</p>
    </address>
  </section>
  <div class="photo photo-concrete" role="img" aria-label="Dunkle Betonwand mit Sideboard und Vase, Blick ins Grüne"></div>
</body>
</html>
```